VELMOT, Time tracking , Timesheet, expenses and invoices management

VELMOT is an online tool to manage company employee time tracking per week or month, also employee time off (vacation), employee , employee expenses and company invoices.

We are about to put our application online and we need a beautiful Landscape page.

We want a single welcome page (somthing like this one http://brindlepixel.example/corvanta_admin-v2.6.2.1/landing.html)

This main page should describe our activities, the subscription pricing ,......

You can take a look briefly to the application here (https://velmot-test.quarnhost.example/). The current Home is just a template and we would like to replace it.

The page must be responsive.

Target Market(s)

Start up , services company, Time sheet,

Industry/Entity Type

It Company

Coding

Coded - Design and coding required

Number of Pages Required

1 page

Font styles to use
Sans Serif

Colors
0455a3
33a6d7
ffffff
abd036

Requirements
Must have
• pricing table, responsive page
• The landing page must indicate that the application handle Task timer, Timesheet, employe expenses, invoice

```html
<!DOCTYPE html>
<html lang="en">
<head>
<meta charset="utf-8">
<title>VELMOT — Time tracking, timesheets, expenses and invoices</title>
<link rel="stylesheet" href="https://fonts.googleapis.com/css2?family=Hind:wght@300;400;500;600;700&family=Open+Sans:wght@400;600&display=swap">
<style>
:root{
  --navy:#0b2a66;
  --navy-2:#15408c;
  --navy-mid:#123a80;
  --title-navy:#17306b;
  --green:#74c043;
  --blue:#33a6d7;
  --white:#ffffff;
  --light:#f4f4f4;
  --card-border:#e2e2e2;
  --text:#444a52;
  --muted:#8a8f96;
  --footer:#2d333b;
  --footer-text:#b8bcc2;
  --copyright:#4b5057;
  --grey-band:#6b6b6b;
  --grey-band-2:#8a8a8a;
}
*{box-sizing:border-box;margin:0;padding:0}
html,body{width:1200px;height:3543px;overflow:hidden}
body{position:relative;font-family:"Open Sans",sans-serif;color:var(--text);background:var(--white)}
.abs{position:absolute}

/* Hero */
.hero{left:0;top:0;width:1200px;height:702px;background:linear-gradient(180deg,var(--navy) 0%,var(--navy-2) 100%);overflow:hidden}
.brand{left:59px;top:40px;font-family:"Hind",sans-serif;font-weight:600;font-size:34px;color:var(--white);letter-spacing:1px}
.nav a{position:absolute;top:52px;font-family:"Hind",sans-serif;font-weight:500;font-size:16px;color:var(--white);text-decoration:none}
.hero-title{left:0;width:1200px;top:198px;text-align:center;font-family:"Hind",sans-serif;font-weight:700;font-size:48px;color:var(--white)}
.hero-sub{left:220px;width:760px;top:266px;text-align:center;font-size:14px;line-height:26px;color:var(--white)}
.hero-shot{left:213px;top:370px;width:716px;height:332px;background:linear-gradient(180deg,#2a2f3a 0 40px,#eef1f4 40px)}

/* How it works */
.how{left:0;top:702px;width:1200px;height:680px;background:var(--light)}
.section-title{left:0;width:1200px;top:62px;text-align:center;font-family:"Hind",sans-serif;font-weight:300;font-size:38px;color:#333;letter-spacing:1px}
.title-rule{left:548px;top:121px;width:84px;height:3px;background:var(--title-navy);margin-left:10px}
.step-card{top:278px;width:333px;height:343px;background:var(--white);border:1px solid var(--card-border);border-radius:14px}
.step-icon{top:183px;width:166px;height:166px;border-radius:50%;border:5px solid var(--green);background:var(--white);display:flex;align-items:center;justify-content:center}
.step-title{position:absolute;left:0;width:100%;top:104px;text-align:center;font-family:"Hind",sans-serif;font-weight:400;font-size:28px;color:#333}
.step-text{position:absolute;left:24px;right:24px;top:160px;text-align:center;font-size:14px;line-height:27px;color:var(--muted)}

/* Easy to customize */
.customize{left:0;top:1382px;width:1200px;height:465px;background:var(--white)}
.customize-shot{left:52px;top:94px;width:620px;height:290px;background:linear-gradient(135deg,#f3f6f9 0%,#dfe9f1 60%,#33a6d7 100%);border-radius:4px}
.feature-title{font-family:"Hind",sans-serif;font-weight:600;font-size:36px;color:var(--title-navy)}
.feature-tag{left:711px;top:137px;font-size:14px;color:var(--muted);letter-spacing:1px}
.feature-tag::before{content:"";display:inline-block;width:26px;height:3px;background:var(--blue);vertical-align:middle;margin-right:18px}
.feature-text{font-size:14px;line-height:22px;color:var(--muted)}
.btn{display:flex;align-items:center;justify-content:center;font-family:"Hind",sans-serif;color:var(--white);background:var(--blue);border-radius:3px}

/* Clean design */
.modern{left:0;top:1847px;width:1200px;height:361px;background:#f3f3f3}
.modern-shot{left:579px;top:66px;width:621px;height:295px;background:linear-gradient(180deg,#e9e9e9 0%,#d6d6d6 100%)}

/* Pricing */
.pricing{left:0;top:2208px;width:1200px;height:863px;background:var(--light)}
.pricing-band{left:0;top:0;width:1200px;height:442px;background:linear-gradient(180deg,var(--navy) 0%,var(--navy-2) 100%)}
.pricing-title{left:0;width:1200px;top:62px;text-align:center;font-family:"Hind",sans-serif;font-weight:600;font-size:38px;color:var(--white)}
.pricing-rule{left:208px;width:767px;top:128px;height:1px;background:rgba(255,255,255,.45)}
.pricing-sub{left:0;width:1200px;top:118px;text-align:center;font-size:14px;color:var(--white)}
.pricing-sub span{background:var(--navy-mid);padding:0 12px}
.plan{top:189px;height:560px;background:var(--white);border-radius:4px;box-shadow:0 2px 8px rgba(0,0,0,.12);overflow:hidden}
.plan-name{height:71px;background:#f0f0f0;display:flex;align-items:center;justify-content:center;font-family:"Hind",sans-serif;font-weight:600;font-size:22px;color:#333}
.plan-band{height:182px;background:var(--grey-band);clip-path:polygon(0 0,100% 0,100% 78%,50% 100%,0 78%);text-align:center;color:var(--white);padding-top:20px}
.plan-band.featured{background:var(--green)}
.plan-band.light{background:var(--grey-band-2)}
.price{font-family:"Hind",sans-serif;font-weight:700;font-size:42px;line-height:46px}
.price small{font-size:15px}
.regular{font-size:12px;line-height:16px}
.signup{display:inline-block;margin-top:10px;width:110px;height:33px;line-height:34px;background:var(--white);color:#333;font-family:"Hind",sans-serif;font-weight:600;font-size:14px}
.plan-list{list-style:none;margin-top:10px}
.plan-list li{height:42.5px;line-height:42.5px;text-align:center;font-size:14.5px;color:#444;border-bottom:1px solid #e8e8e8}

/* Help bar */
.help{left:0;top:3071px;width:1200px;height:153px;background:var(--footer)}
.help-tab{left:0;top:0;width:510px;height:153px;background:var(--white);clip-path:polygon(0 0,100% 0,92% 100%,0 100%)}
.help-label{left:195px;top:30px;font-family:"Hind",sans-serif;font-weight:700;font-size:18px;color:#333}
.help-label span{font-weight:400;color:var(--muted)}
.help-phone{left:59px;top:50px;font-family:"Hind",sans-serif;font-weight:700;font-size:46px;color:var(--green)}
.news-label{left:593px;top:52px;font-size:13px;color:var(--white)}
.news-input{left:593px;top:73px;width:423px;height:45px;background:var(--white);border-radius:2px;padding-left:14px;display:flex;align-items:center;font-size:12px;color:#999}
.news-btn{left:1030px;top:73px;width:104px;height:45px;background:#8a9099;color:var(--white);display:flex;align-items:center;justify-content:center;font-family:"Hind",sans-serif;font-weight:600;font-size:14px}

/* Footer */
.footer{left:0;top:3224px;width:1200px;height:279px;background:var(--footer)}
.footer-brand{left:59px;top:28px;font-family:"Hind",sans-serif;font-weight:600;font-size:32px;color:var(--white);letter-spacing:1px}
.footer-about{left:59px;top:96px;width:250px;font-size:12px;line-height:20px;color:var(--footer-text)}
.footer-head{top:52px;font-family:"Hind",sans-serif;font-weight:700;font-size:13px;letter-spacing:1px;color:var(--white)}
.footer-head::after{content:"";display:block;width:56px;height:2px;background:var(--green);margin-top:6px}
.post-thumb{left:328px;width:55px;height:50px;background:linear-gradient(135deg,#7e8b97,#c9d2da)}
.post-title{left:397px;font-size:12.5px;color:var(--white)}
.post-meta{left:410px;font-size:10px;color:#8a9099}
.tag{font-size:11px;color:var(--footer-text)}
.sub-input{left:869px;top:104px;width:236px;height:40px;border:1px solid #6a7079;border-radius:20px;padding-left:16px;display:flex;align-items:center;font-size:12px;color:#8a9099}
.sub-btn{left:1018px;top:107px;width:84px;height:34px;border-radius:17px;background:var(--green);color:var(--white);display:flex;align-items:center;justify-content:center;font-size:13px;font-weight:600}
.social{top:192px;width:14px;height:14px;border-radius:50%;border:2px solid var(--footer-text)}
.copyright{left:0;top:3503px;width:1200px;height:40px;background:var(--copyright);color:var(--white);font-size:13px;display:flex;align-items:center;justify-content:center}
</style>
</head>
<body>

<header class="abs hero">
  <div class="abs brand">VELMOT</div>
  <nav class="nav">
    <a style="left:572px">Home</a>
    <a style="left:659px">How it work</a>
    <a style="left:791px">Features</a>
    <a style="left:898px">Pricing</a>
    <a style="left:994px">FAQ</a>
    <a style="left:1065px">Contact</a>
  </nav>
  <h1 class="abs hero-title">VELMOT - Time Tracking &amp; Invoicing</h1>
  <p class="abs hero-sub">Track tasks with a timer, fill weekly or monthly timesheets, manage time off and employee expenses, and send company invoices from one simple online tool.</p>
  <div class="abs hero-shot" role="img" aria-label="Time tracking dashboard preview with sidebar menu, stat tiles and hours chart"></div>
</header>

<section class="abs how">
  <h2 class="abs section-title">HOW IT WORKS ?</h2>
  <div class="abs title-rule"></div>

  <article class="abs step-card" style="left:59px">
    <h3 class="step-title">Task Timer</h3>
    <p class="step-text">Start the timer on any task with one click. Every minute is logged to the right project, so nothing slips away at the end of the day.</p>
  </article>
  <article class="abs step-card" style="left:432px">
    <h3 class="step-title">Timesheets</h3>
    <p class="step-text">Employees fill timesheets per week or month, add vacation and time off, and managers approve them in a few seconds.</p>
  </article>
  <article class="abs step-card" style="left:808px">
    <h3 class="step-title">Expenses &amp; Invoices</h3>
    <p class="step-text">Record employee expenses with receipts and turn tracked hours into clean company invoices ready to send to clients.</p>
  </article>

  <div class="abs step-icon" style="left:143px">
    <svg width="70" height="70" viewBox="0 0 70 70"><rect x="2" y="2" width="32" height="32" fill="#3a3f47"/><rect x="36" y="2" width="32" height="32" fill="#3a3f47"/><rect x="2" y="36" width="32" height="32" fill="#3a3f47"/><rect x="36" y="36" width="32" height="32" fill="#2f8fd8"/></svg>
  </div>
  <div class="abs step-icon" style="left:516px">
    <svg width="84" height="74" viewBox="0 0 84 74"><rect x="4" y="8" width="76" height="48" fill="none" stroke="#111" stroke-width="6"/><rect x="34" y="56" width="16" height="10" fill="#111"/><rect x="22" y="66" width="40" height="5" fill="#111"/><path d="M30 42 L62 10 L68 16 L36 48 L28 50 Z" fill="#111"/></svg>
  </div>
  <div class="abs step-icon" style="left:891px">
    <svg width="70" height="70" viewBox="0 0 70 70"><rect x="6" y="44" width="10" height="22" fill="#2c3038"/><rect x="22" y="34" width="10" height="32" fill="#2c3038"/><rect x="38" y="38" width="10" height="28" fill="#2c3038"/><rect x="54" y="24" width="10" height="42" fill="#2c3038"/><path d="M8 32 L26 16 L40 26 L60 6" fill="none" stroke="#2c3038" stroke-width="5"/><path d="M50 4 L64 2 L62 16 Z" fill="#2c3038"/></svg>
  </div>
</section>

<section class="abs customize">
  <div class="abs customize-shot" role="img" aria-label="Laptop and phone showing team hours report with circular stats and area chart"></div>
  <h2 class="abs feature-title" style="left:711px;top:88px">Easy to Customize</h2>
  <p class="abs feature-tag">Make it your own</p>
  <p class="abs feature-text" style="left:711px;top:179px;width:430px">Simple. Intuitive. No expertise required to log hours, submit a timesheet or file an expense. Set your own projects, rates and approval steps so VELMOT fits the way your team works.</p>
  <div class="abs btn" style="left:711px;top:302px;width:142px;height:38px;font-size:12px;letter-spacing:1px">
    <svg width="12" height="12" viewBox="0 0 12 12" style="margin-right:7px"><circle cx="6" cy="6" r="6" fill="#fff"/><path d="M5 3.5 L8.5 6 L5 8.5 Z" fill="#33a6d7"/></svg>TAKE A TOUR
  </div>
</section>

<section class="abs modern">
  <h2 class="abs feature-title" style="left:76px;top:58px;font-size:29px">Clean &amp; Ultra Modern Design</h2>
  <p class="abs feature-text" style="left:76px;top:106px;width:470px;font-size:13px;color:#555">One clear screen for your whole week: running timers, open timesheets and pending expenses at a glance.</p>
  <p class="abs feature-text" style="left:76px;top:168px;width:470px;font-size:13px;color:#555">→ Approve timesheets and time off requests, and see who is on vacation this week.</p>
  <p class="abs feature-text" style="left:76px;top:226px;width:470px;font-size:13px;color:#555">→ Turn approved hours and expenses into invoices in one step.</p>
  <div class="abs btn" style="left:87px;top:297px;width:145px;height:38px;font-size:15px">Buy Now</div>
  <div class="abs modern-shot" role="img" aria-label="Hands holding a tablet that plays a walkthrough of the timesheet dashboard"></div>
</section>

<section class="abs pricing">
  <div class="abs pricing-band"></div>
  <h2 class="abs pricing-title">Simple Pricing</h2>
  <div class="abs pricing-rule"></div>
  <p class="abs pricing-sub"><span>For big and small companies</span></p>

  <article class="abs plan" style="left:78px;width:300px">
    <div class="plan-name">STARTER PACK</div>
    <div class="plan-band">
      <div class="price">$9.75<small>/M</small></div>
      <div class="regular">Regularly <s>$16.99</s></div>
      <div class="signup">SIGN UP</div>
    </div>
    <ul class="plan-list"><li>$16 / month</li><li>Task timer</li><li>Timesheets</li><li>Time off</li><li>Expenses</li><li>Invoices</li></ul>
  </article>
  <article class="abs plan" style="left:439px;width:312px">
    <div class="plan-name">STARTER PACK</div>
    <div class="plan-band featured">
      <div class="price">$9.75<small>/M</small></div>
      <div class="regular">Regularly <s>$16.99</s></div>
      <div class="signup">SIGN UP</div>
    </div>
    <ul class="plan-list"><li>$16 / month</li><li>Task timer</li><li>Timesheets</li><li>Time off</li><li>Expenses</li><li>Invoices</li></ul>
  </article>
  <article class="abs plan" style="left:808px;width:314px">
    <div class="plan-name">STARTER PACK</div>
    <div class="plan-band light">
      <div class="price">$9.75<small>/M</small></div>
      <div class="regular">Regularly <s>$16.99</s></div>
      <div class="signup">SIGN UP</div>
    </div>
    <ul class="plan-list"><li>$16 / month</li><li>Task timer</li><li>Timesheets</li><li>Time off</li><li>Expenses</li><li>Invoices</li></ul>
  </article>
</section>

<section class="abs help">
  <div class="abs help-tab"></div>
  <div class="abs help-label">NEED HELP? <span>CALL US 24/7:</span></div>
  <div class="abs help-phone">+1 555-014-7290</div>
  <div class="abs news-label">Sign up to Newsletter for get special offers</div>
  <div class="abs news-input">Please enter your email...</div>
  <div class="abs news-btn">SIGN UP</div>
</section>

<footer class="abs footer">
  <div class="abs footer-brand">VELMOT</div>
  <p class="abs footer-about">Appvane is a creative &amp; unique App Multipurpose LandingPage Pressly Theme for App Showcase &amp; App Market.<br><br>The theme is proudly featured on Foliora community for its interaction.</p>

  <div class="abs footer-head" style="left:328px">RECENT POST</div>
  <div class="abs post-thumb" style="top:99px" role="img" aria-label="Blog post thumbnail"></div>
  <div class="abs post-title" style="top:104px">A Mindful Shift Of Focus</div>
  <div class="abs post-meta" style="top:128px">Admin · 24 Nov 2016</div>
  <div class="abs post-thumb" style="top:177px" role="img" aria-label="Blog post thumbnail"></div>
  <div class="abs post-title" style="top:182px">The Low Of A Long Walk</div>
  <div class="abs post-meta" style="top:206px">Admin · 24 Nov 2016</div>

  <div class="abs footer-head" style="left:600px">TAGS</div>
  <span class="abs tag" style="left:612px;top:110px">challenging</span>
  <span class="abs tag" style="left:704px;top:110px">the world</span>
  <span class="abs tag" style="left:612px;top:146px">trending</span>
  <span class="abs tag" style="left:690px;top:146px">blue</span>
  <span class="abs tag" style="left:749px;top:146px">travelling</span>
  <span class="abs tag" style="left:612px;top:184px">places</span>
  <span class="abs tag" style="left:678px;top:184px">fooding</span>

  <div class="abs footer-head" style="left:869px">SUBSCRIBE TO NEWSLETTER</div>
  <div class="abs sub-input">Email Address</div>
  <div class="abs sub-btn">Submit</div>
  <span class="abs social" style="left:876px"></span>
  <span class="abs social" style="left:914px"></span>
  <span class="abs social" style="left:952px"></span>
  <span class="abs social" style="left:990px"></span>
  <span class="abs social" style="left:1028px"></span>
</footer>

<div class="abs copyright">Copyright © 2016 - Velmot. All rights reserved.</div>

</body>
</html>
```